Oakmere Kin Clinic

We are a doctors surgery, providing medical services to all ages

we aim for a professional as well as an eye catching look for the signs that can be seen by passing vehicles and people who walk by

trustworthy quality medical care to to all patients, we treat like family

Name- Brenwick Kin Clinic Medical practice

Target Market(s)

all ages, adults
the elderly

Industry/Entity Type

Medical

Requirements
Must have
• eye catching,
obvious medical service location

```html
<!DOCTYPE html>
<html lang="en">
<head>
<meta charset="utf-8">
<title>Brenwick Kin Clinic – Street Sign</title>
<link rel="stylesheet" href="https://fonts.googleapis.com/css2?family=Cinzel:wght@700&family=Open+Sans:wght@700;800&display=swap">
<style>
  :root {
    --backdrop: #c4bd68;
    --gold-light: #fff3a8;
    --gold-mid: #f3c928;
    --gold-deep: #c8901a;
    --title-blue-top: #3a7fd8;
    --title-blue-bottom: #1b2f8f;
    --title-green-top: #7fcf4a;
    --title-green-bottom: #2f9a2a;
    --pill-pink-top: #f78ac6;
    --pill-pink: #e0248f;
    --tagline-navy: #2b2170;
    --logo-blue: #1c7fc4;
    --white: #ffffff;
  }
  * { margin: 0; padding: 0; box-sizing: border-box; }
  html, body { width: 1200px; height: 614px; overflow: hidden; background: var(--backdrop); }
  .canvas { position: relative; width: 1200px; height: 614px; }

  .sign {
    position: absolute; left: 64px; top: 160px; width: 1063px; height: 284px;
    filter: drop-shadow(5px 6px 5px rgba(0,0,0,.35));
  }
  .sign-bands { position: absolute; inset: 0; width: 100%; height: 100%; }

  .clinic-mark {
    position: absolute; left: 20px; top: 47px; width: 158px; height: 158px;
    display: flex; align-items: center; justify-content: center; text-align: center;
  }
  .clinic-mark-ring {
    position: absolute; inset: 0; border-radius: 50%;
    border: 8px solid var(--logo-blue);
  }
  .clinic-mark-name {
    position: relative; font-family: "Cinzel", serif; font-weight: 700;
    font-size: 20px; line-height: 1.15; color: var(--logo-blue); width: 120px;
  }

  .care-photo {
    position: absolute; left: 741px; top: 29px; width: 322px; height: 202px;
    background:
      radial-gradient(ellipse at 22% 45%, #f1ece6 0 30%, transparent 55%),
      radial-gradient(ellipse at 70% 55%, #b9cde6 0 30%, transparent 60%),
      linear-gradient(90deg, #eef2f6, #c9d6e6 60%, #dfe6ee);
  }

  .clinic-title {
    position: absolute; z-index: 1; left: 186px; top: 42px; width: 610px; text-align: center;
    font-family: "Cinzel", serif; font-weight: 700; line-height: 1;
  }
  .clinic-title span {
    display: block; white-space: nowrap;
    -webkit-background-clip: text; background-clip: text; color: transparent;
    filter: drop-shadow(1px 2px 1px rgba(0,0,0,.25));
  }
  .clinic-name {
    font-size: 52px;
    background-image: linear-gradient(var(--title-blue-top), var(--title-blue-bottom));
  }
  .clinic-type {
    font-size: 62px; margin-top: 2px;
    background-image: linear-gradient(var(--title-green-top), var(--title-green-bottom));
  }

  .phone-pill {
    position: absolute; left: 286px; top: 178px; width: 403px; height: 44px;
    border-radius: 22px;
    background: linear-gradient(var(--pill-pink-top), var(--pill-pink) 55%, #c81a7c);
    display: flex; align-items: center; justify-content: center; gap: 14px;
    font-family: "Open Sans", sans-serif; font-weight: 800; font-size: 36px;
    color: var(--white); letter-spacing: 1px;
    text-shadow: 1px 2px 2px rgba(0,0,0,.35);
  }
  .phone-icon { width: 34px; height: 30px; }

  .tagline {
    position: absolute; left: 0; right: 0; top: 259px; transform: translateY(-50%);
    text-align: center; line-height: 1;
    font-family: "Open Sans", sans-serif; font-weight: 700; font-size: 32px;
    letter-spacing: 1px; color: var(--tagline-navy);
  }
</style>
</head>
<body>
<main class="canvas">
  <section class="sign">
    <svg class="sign-bands" viewBox="0 0 1063 284" preserveAspectRatio="none" aria-hidden="true">
      <defs>
        <linearGradient id="goldBand" x1="0" y1="0" x2="0" y2="1">
          <stop offset="0" stop-color="var(--gold-deep)"/>
          <stop offset="0.45" stop-color="var(--gold-light)"/>
          <stop offset="1" stop-color="var(--gold-mid)"/>
        </linearGradient>
      </defs>
      <rect x="0" y="0" width="1063" height="284" fill="url(#goldBand)"/>
      <path d="M0 18 Q260 4 560 12 T1063 8 L1063 228 Q700 222 400 226 T0 226 Z" fill="var(--white)"/>
    </svg>

    <div class="clinic-mark">
      <div class="clinic-mark-ring"></div>
      <p class="clinic-mark-name">Oakmere Kin Clinic</p>
    </div>

    <div class="care-photo" role="img" aria-label="Photo of a smiling doctor in a white coat with a stethoscope beside a multi-generation family"></div>

    <h1 class="clinic-title">
      <span class="clinic-name">Brenwick Kin Clinic</span>
      <span class="clinic-type">Medical Practice</span>
    </h1>

    <p class="phone-pill">
      <svg class="phone-icon" viewBox="0 0 34 30" aria-hidden="true">
        <path d="M2 9 Q17 -2 32 9 L28 13 L23 10 L23 7 Q17 5 11 7 L11 10 L6 13 Z" fill="var(--white)"/>
        <path d="M9 14 L25 14 L30 27 L4 27 Z" fill="var(--white)"/>
        <circle cx="17" cy="20" r="4" fill="var(--pill-pink)"/>
      </svg>
      <span>9488 2130</span>
    </p>

    <p class="tagline">Trustworthy medical care for all patients</p>
  </section>
</main>
</body>
</html>
```